Personal Development Book for Millennials Needs a Cover Design

Book Title: Salt Horizon: A Dreamer's Map to Being, 15 "No Escape" Queries on Joy, Routines and Grit for Muddled Millennials
Author's Name: Marcus T. Oldenfrey
Salt Horizon: A Dreamer's Map to Being is a collection of raw, unfiltered and personal essays on happiness, habits and hustle. It is a compilation of 15 provocative, yet fundamental questions that every mixed-up millennial or twenty-something should answer in order to live a life full of energy and excitement rather than monotony and mediocrity.
It is a personal development book written by a regular, twenty-something dude who got tired of doing boring things. He then quit his job, fell off a motorcycle somewhere near the equator, and came back to the States and immediately started writing.
"Pura vida," the law of the land in Costa Rica, translates to "pure life." "Pura vida" is more than just a greeting; it is an embodiment of the Costa Rican people, who find immense happiness in life's little pleasures, preferring to lay low, live slow and live purposefully. "Pura vida" is another way of saying "relax and take it easy."
The goal of the book is to stand out on the Zelvora platform as a small thumbnail. The imagery should make the viewer feel that the book (and the author) is an authority on the topic of self-discovery, self-awareness, and purposeful, intentional living.
The reader should feel that they MUST read this book if they are the least bit confused, anxious, mixed-up or desperately trying to figure out how to take back control of their own life and start doing the things that excite them. It's more important that the book "pops off the shelf" or stands out and catches the eye quickly.
The most important part of the design is that it is clean, uncluttered and simple. It should embody the "pura vida" lifestyle. I am open to any image or illustration you choose.
I like a bold color palette, and I'd like to see green be the primary color used in the design. Lush, greenery is everywhere in Costa Rica. Green also represents life, very appropriate for this book. I like bold titles that are easy to recognize and comprehend. Please use no more than 2-3 colors.
Zelvora eBook covers I particularly like:
Print Liftoff by Wesley Harrow
A Man Near The Pier by Neil Dorsey
Inner Steel — 48 Tested Paths to Build Inner Steel, Lift Your Morale and Quiet Inner Worry by Rory M.T. Pask
Hour Mastery: Peak Output by Owen Farrukh
Target Market(s)
Millennials
Requirements
Must have
- This book is intended to encourage millennials to do some soul-searching, think and WRITE down their own answers to the questions in this book. It is a book that should be read with a notebook and a pen close by.
- I'd like to see covers that subtly hint at this fact. Please reference the example covers listed in the project description to best match the style of cover I am looking for. If it is clear that you have NOT referenced the example covers, your design will be eliminated.
Nice to have
- If possible, would like to see designs that include the following three components WITHOUT making the cover feel too busy or cluttered:
- 1) Pen
- 2) Paper
- 3) Beach
Should not have
- Cover should NOT look or feel as if this is a book about environmentalism. Trees, plants, greenery, etc. should NOT be the primary focal point of the cover design. If included, these elements should be additive.

```html
<!DOCTYPE html>
<html lang="en">
<head>
<meta charset="utf-8">
<title>Salt Horizon: A Dreamer's Map to Being</title>
<link rel="stylesheet" href="https://fonts.googleapis.com/css2?family=Oswald:wght@400;500;700&display=swap">
<style>
  :root {
    --green-light: #b4e65a;
    --green-mid: #8fd13a;
    --green-deep: #6db22a;
    --band-purple: #6b2fa3;
    --text-white: #ffffff;
    --author-green: #1f3d17;
  }
  html, body {
    margin: 0;
    padding: 0;
    overflow: hidden;
    background: #ffffff;
  }
  .cover {
    position: relative;
    width: 703px;
    height: 1200px;
    overflow: hidden;
    font-family: "Oswald", sans-serif;
  }
  .cover__backdrop {
    position: absolute;
    inset: 0;
    background:
      linear-gradient(135deg, rgba(255,255,255,0.10) 0%, rgba(255,255,255,0) 40%),
      linear-gradient(200deg, var(--green-light) 0%, var(--green-mid) 45%, var(--green-deep) 100%);
  }
  .subtitle {
    position: absolute;
    top: 40px;
    left: 0;
    width: 100%;
    margin: 0;
    text-align: center;
    color: var(--text-white);
    font-weight: 500;
    font-size: 40px;
    line-height: 52px;
    letter-spacing: 0.2px;
  }
  .subtitle span { display: block; }
  .title {
    position: absolute;
    left: 0;
    top: 0;
    width: 703px;
    height: 1200px;
  }
  .title__word {
    fill: var(--text-white);
    font-family: "Oswald", sans-serif;
    font-weight: 400;
    font-size: 270px;
  }
  .title__band {
    fill: var(--band-purple);
  }
  .title__tagline {
    fill: var(--text-white);
    font-family: "Oswald", sans-serif;
    font-weight: 500;
    font-size: 50px;
    letter-spacing: 1px;
  }
  .author {
    position: absolute;
    top: 950px;
    left: 0;
    width: 100%;
    margin: 0;
    text-align: center;
    color: var(--author-green);
    font-weight: 700;
    font-size: 62px;
    letter-spacing: 1px;
  }
</style>
</head>
<body>
  <div class="cover">
    <div class="cover__backdrop" role="img" aria-label="Bright green low-poly faceted background"></div>

    <p class="subtitle">
      <span>15 “No Escape” Queries</span>
      <span>on Joy, Routines and Grit</span>
      <span>for Muddled Millennials</span>
    </p>

    <svg class="title" viewBox="0 0 703 1200" aria-label="Salt Horizon: A Dreamer's Map to Being">
      <text class="title__word" x="47" y="422" textLength="609" lengthAdjust="spacingAndGlyphs">SALT</text>
      <g transform="rotate(-2 430 468)">
        <rect class="title__band" x="158" y="432" width="580" height="72"/>
        <text class="title__tagline" x="182" y="487" textLength="500" lengthAdjust="spacingAndGlyphs">A DREAMER’S MAP TO BEING</text>
      </g>
      <text class="title__word" x="36" y="716" textLength="631" lengthAdjust="spacingAndGlyphs">HORIZON</text>
    </svg>

    <p class="author">MARCUS T. OLDENFREY</p>
  </div>
</body>
</html>
```